Velorin Banner Design

We need banners for new company Velorin Holdings Limited located in Hong Kong. Velorin is an global online business platform, needs clean white, blue and red color mix banners.

Reason: I am extending for final design

Target Market(s)

Velorin an online Business Company have a target home based business owners and DIY website seekers.

Industry/Entity Type

Business

Colors
0355a3
ec2027
ffffff

Requirements
Must have
• Free Sign Up Button and Velorin Logo

```html
<!DOCTYPE html>
<html lang="en">
<head>
<meta charset="utf-8">
<title>Velorin Banner Set</title>
<link rel="stylesheet" href="https://fonts.googleapis.com/css2?family=Roboto+Condensed:wght@400;700&display=swap">
<style>
:root{
  --blue:#0355a3;
  --blue-deep:#02468a;
  --blue-light:#2a7fd0;
  --red:#ec2027;
  --red-deep:#c4141a;
  --white:#ffffff;
  --logo-grey:#8c8c8c;
  --board-edge:#a9a9a9;
}
*{margin:0;padding:0;box-sizing:border-box}
html,body{width:1200px;height:903px;overflow:hidden}
body{font-family:"Roboto Condensed",Arial,sans-serif;background:var(--board-edge)}
.board{position:relative;width:1200px;height:903px;
  background:radial-gradient(ellipse at 45% 40%,#e6e6e6 0%,#d2d2d2 55%,#b4b4b4 100%);
  box-shadow:inset 0 0 0 8px #c4c4c4}
.watermark-name{position:absolute;left:128px;top:662px;font-size:112px;font-weight:700;
  letter-spacing:6px;color:rgba(110,110,110,.45)}

.banner{position:absolute;background:linear-gradient(180deg,var(--blue-light) 0%,var(--blue) 45%,var(--blue-deep) 100%);
  border:3px solid var(--white);outline:3px solid var(--blue);
  color:var(--white);text-align:center;display:flex;flex-direction:column;align-items:center;overflow:hidden}
.head{width:100%;background:var(--white);display:flex;align-items:center;justify-content:center;
  border-radius:0 0 50% 50% / 0 0 14px 14px;flex:none}
.brand{font-weight:700;color:var(--logo-grey);letter-spacing:1px;line-height:1}
.hot{color:var(--red);font-weight:700;
  text-shadow:-1px -1px 0 var(--white),1px -1px 0 var(--white),-1px 1px 0 var(--white),1px 1px 0 var(--white)}
.line{font-weight:700;line-height:1.1}
.thin{font-weight:400}
.signup{background:linear-gradient(180deg,#ff3a40 0%,var(--red) 50%,var(--red-deep) 100%);
  border:2px solid var(--white);color:var(--white);font-weight:700;line-height:1;flex:none}

/* small square */
.b-square{left:102px;top:64px;width:152px;height:112px}
.b-square .head{height:30px}
.b-square .brand{font-size:20px}
.b-square .line{font-size:13px;margin-top:9px}
.b-square .price{font-size:16px;margin-top:4px}
.b-square .signup{font-size:13px;padding:3px 8px;margin-top:6px}

/* leaderboard */
.b-leader{left:279px;top:64px;width:596px;height:74px;flex-direction:row;align-items:stretch}
.b-leader .head{width:150px;height:auto;border-radius:0 50% 50% 0 / 0 50% 50% 0}
.b-leader .brand{font-size:25px}
.b-leader .copy{flex:1;display:flex;flex-direction:column;justify-content:center;
  align-items:flex-start;padding-left:14px;white-space:nowrap}
.b-leader .hot{font-size:22px;line-height:1.1}
.b-leader .line{font-size:17px;margin-top:3px}
.b-leader .signup{align-self:center;margin-right:10px;padding:6px 10px;font-size:18px}

/* tall small */
.b-tall{left:102px;top:199px;width:152px;height:203px}
.b-tall .head{height:36px}
.b-tall .brand{font-size:22px}
.b-tall .hot{font-size:17px;line-height:1.05;margin-top:10px}
.b-tall .price{font-size:22px;margin-top:4px}
.b-tall .line{font-size:13px;margin-top:8px}
.b-tall .signup{font-size:16px;padding:4px 9px;margin-top:10px}

/* medium rectangle */
.b-medium{left:295px;top:199px;width:319px;height:318px}
.b-medium .head{height:70px}
.b-medium .brand{font-size:38px;margin-top:-6px}
.b-medium .thin{font-size:19px;margin-top:2px}
.b-medium .line{font-size:21px}
.b-medium .hot{font-size:25px;margin-top:4px}
.b-medium .earn{font-size:17px;margin-top:8px}
.b-medium .big{font-size:29px;margin-top:12px}
.b-medium .sub{font-size:21px}
.b-medium .signup{font-size:24px;padding:5px 14px;margin-top:14px}

/* square */
.b-block{left:655px;top:199px;width:158px;height:158px}
.b-block .head{height:36px}
.b-block .brand{font-size:22px}
.b-block .hot{font-size:17px;line-height:1.05;margin-top:10px}
.b-block .price{font-size:22px;margin-top:4px}
.b-block .signup{font-size:16px;padding:4px 9px;margin-top:6px}

/* skyscraper */
.b-sky{left:902px;top:64px;width:203px;height:763px}
.b-sky .head{height:76px}
.b-sky .brand{font-size:36px}
.b-sky .thin{font-size:23px;margin-top:20px}
.b-sky .line{font-size:30px}
.b-sky .at{font-size:70px;font-weight:400;color:rgba(190,220,255,.75);line-height:1;margin-top:4px}
.b-sky .hot{line-height:1}
.b-sky .min{font-size:34px}
.b-sky .ten{font-size:96px;line-height:.9}
.b-sky .ten sup{font-size:40px;vertical-align:top;position:relative;top:8px}
.b-sky .per{font-size:28px}
.b-sky .rev{font-size:26px;margin-top:46px}
.b-sky .mid{font-size:27px;margin-top:12px}
.b-sky .aff{font-size:34px;font-weight:400;margin-top:8px}
.b-sky .prog{font-size:31px;margin-top:4px}
.b-sky .signup{font-size:38px;padding:10px 24px;margin-top:28px;line-height:.95}
.b-sky .signup small{display:block;font-size:24px}
</style>
</head>
<body>
<main class="board">
  <div class="watermark-name">VELORIN</div>

  <section class="banner b-square">
    <div class="head"><span class="brand">VELORIN</span></div>
    <div class="line">eCOMMERCE WEBSITE</div>
    <div class="line price">@ $10/Month</div>
    <div class="signup">FREE SIGN UP</div>
  </section>

  <section class="banner b-leader">
    <div class="head"><span class="brand">VELORIN</span></div>
    <div class="copy">
      <div class="hot">eCOMMERCE WEBSITE @ $10/Month</div>
      <div class="line">Revolutionary Single Line Affiliate Program</div>
    </div>
    <div class="signup">FREE<br>SIGN UP</div>
  </section>

  <section class="banner b-tall">
    <div class="head"><span class="brand">VELORIN</span></div>
    <div class="hot">eCOMMERCE<br>WEBSITE</div>
    <div class="hot price">@ $10/Month</div>
    <div class="line">Revolutionary Single<br>Line Affiliate Program</div>
    <div class="signup">FREE SIGN UP</div>
  </section>

  <section class="banner b-medium">
    <div class="head"><span class="brand">VELORIN</span></div>
    <div class="thin">Create Your Own</div>
    <div class="line">eCOMMERCE WEBSITE</div>
    <div class="hot">@ Minimum $10/Month</div>
    <div class="line earn">&amp; Start Earning <span class="thin">at the Same Time.</span></div>
    <div class="line big">Revolutionary</div>
    <div class="line sub">Single Line Affiliate Program</div>
    <div class="signup">FREE SIGN UP</div>
  </section>

  <section class="banner b-block">
    <div class="head"><span class="brand">VELORIN</span></div>
    <div class="hot">eCOMMERCE<br>WEBSITE</div>
    <div class="hot price">@ $10/Month</div>
    <div class="signup">FREE SIGN UP</div>
  </section>

  <section class="banner b-sky">
    <div class="head"><span class="brand">VELORIN</span></div>
    <div class="thin">Create Your Own</div>
    <div class="line">eCOMMERCE<br>WEBSITE</div>
    <div class="at">@</div>
    <div class="hot min">MINIMUM</div>
    <div class="hot ten"><sup>$</sup>10</div>
    <div class="hot per">PER MONTH</div>
    <div class="line rev">REVOLUTIONARY</div>
    <div class="line mid">Single Line</div>
    <div class="aff">AFFILIATE</div>
    <div class="line prog">Program</div>
    <div class="signup">FREE<small>SIGN UP</small></div>
  </section>
</main>
</body>
</html>
```